Forest Consultant/Timber Buyer needs a clean business card

We are a forestry consulting and timber buying company. We meet with private landowners and assist them with timber management and timber harvesting. We would like a professional business card, please no clip art. logo is blue and white but would like to see a gray,silver, or some other color incorporated. Would like basic contact info. Would like to the layout to be creative and sleek but masculine.

Target Market(s)

private landowners

Industry/Entity Type

Business

Contact Information for Business Card

name,position, cell number, office number, email, website. This might be to cluttered. Basic contact info is what we are looking for.

Contact info can all be on one side with logo on the other.

Font styles to use
Serif
Sans Serif

Colors
0255a3
ffffff
aaaaaa

Requirements
Must have
• We just want it professional.
Nice to have
• Creative layout.
Should not have
• please no clip art of log trucks etc.

```html
<!DOCTYPE html>
<html lang="en">
<head>
<meta charset="utf-8">
<title>Ashgrove Land &amp; Timber – Business Card</title>
<link href="https://fonts.googleapis.com/css2?family=Open+Sans:wght@400;600;700&display=swap" rel="stylesheet">
<style>
  :root {
    --brand-blue: #0e4f96;
    --brand-blue-deep: #0b468a;
    --silver: #5c6068;
    --text-grey: #4a4a4a;
    --paper: #ffffff;
    --backdrop: #e9e7e4;
  }
  * { box-sizing: border-box; margin: 0; padding: 0; }
  html, body {
    width: 1200px; height: 1000px; overflow: hidden;
    background: var(--backdrop);
    font-family: "Open Sans", Arial, sans-serif;
  }
  .card {
    position: absolute; left: 265px; width: 667px; height: 398px;
    border-radius: 22px; overflow: hidden;
    box-shadow: 0 4px 14px rgba(0,0,0,0.18);
  }
  .card--front { top: 73px; background: var(--paper); }
  .card--back { top: 532px; background: var(--brand-blue); }

  .wordmark { position: absolute; display: flex; align-items: center; gap: 14px; font-weight: 700; }
  .wordmark__dot { width: 58px; height: 58px; border-radius: 50%; background: var(--brand-blue); }
  .wordmark__text { display: flex; flex-direction: column; align-items: flex-end; line-height: 1; }
  .wordmark__name { font-size: 44px; letter-spacing: 1px; }
  .wordmark__sub { font-size: 14px; letter-spacing: 3px; margin-top: 6px; }

  .card--front .wordmark { left: 34px; top: 62px; color: var(--brand-blue); }
  .card--back .wordmark { right: 34px; bottom: 34px; color: var(--paper); }
  .card--back .wordmark__name { font-size: 46px; letter-spacing: 2px; }
  .card--back .wordmark__sub { align-self: center; }

  .person { position: absolute; right: 34px; top: 204px; text-align: right; }
  .person__name { color: var(--brand-blue); font-weight: 700; font-size: 20px; letter-spacing: 0.3px; }
  .person__role { color: var(--text-grey); font-size: 15.5px; margin-top: 2px; }

  .contact { position: absolute; left: 34px; top: 232px; list-style: none; }
  .contact li { display: flex; align-items: center; gap: 8px; height: 25px; color: var(--text-grey); font-size: 16px; }
  .contact svg { width: 14px; height: 14px; fill: var(--brand-blue); flex: none; }

  .swoosh { position: absolute; left: 0; bottom: 0; width: 667px; height: 60px; }
</style>
</head>
<body>
  <section class="card card--front">
    <div class="wordmark">
      <span class="wordmark__dot"></span>
      <span class="wordmark__text">
        <span class="wordmark__name">ASHGROVE</span>
        <span class="wordmark__sub">LAND &amp; TIMBER</span>
      </span>
    </div>

    <div class="person">
      <p class="person__name">DANIEL WHITMORE</p>
      <p class="person__role">Managing Director</p>
    </div>

    <ul class="contact">
      <li><svg viewBox="0 0 14 14"><rect x="3.5" y="0" width="7" height="14" rx="1.5"/><rect x="5" y="2" width="4" height="6" fill="#fff"/></svg>+ 000 000 0000</li>
      <li><svg viewBox="0 0 14 14"><path d="M1 5c0-2 3-3 6-3s6 1 6 3v1h-3V4.5H4V6H1z"/><rect x="2.5" y="7" width="9" height="6" rx="1"/></svg>+ 000 000 0000</li>
      <li><svg viewBox="0 0 14 14"><rect x="0.5" y="2.5" width="13" height="9" rx="1"/><path d="M1 3l6 5 6-5" stroke="#fff" stroke-width="1.2" fill="none"/></svg>info@ashgroveland.com</li>
      <li><svg viewBox="0 0 14 14"><circle cx="7" cy="7" r="6.5"/><path d="M0.5 7h13M7 0.5c-3 3-3 10 0 13M7 0.5c3 3 3 10 0 13" stroke="#fff" stroke-width="1" fill="none"/></svg>www.ashgroveland.com</li>
    </ul>

    <svg class="swoosh" viewBox="0 0 667 60" preserveAspectRatio="none" aria-hidden="true">
      <path d="M150 26 Q420 0 667 22 L667 40 Q420 18 200 28 Z" fill="var(--silver)"/>
      <path d="M0 40 Q300 14 667 38 L667 60 L0 60 Z" fill="var(--paper)"/>
      <path d="M0 44 Q300 18 667 42 L667 60 L0 60 Z" fill="var(--brand-blue)"/>
    </svg>
  </section>

  <section class="card card--back">
    <div class="wordmark">
      <span class="wordmark__text">
        <span class="wordmark__name">ASHGROVE</span>
        <span class="wordmark__sub">LAND &amp; TIMBER</span>
      </span>
    </div>
  </section>
</body>
</html>
```